We need visit card and a letter paper for our website. thx

We have a beauty clinic in Switzerland.
https://wiesentalblick.ch
We need a visit card.

Requirements
Must have
• see colors on website

```html
<!DOCTYPE html>
<html lang="de">
<head>
<meta charset="utf-8">
<title>Wiesentalblick – Briefpapier und Visitenkarten</title>
<link rel="stylesheet" href="https://fonts.googleapis.com/css2?family=Montserrat:wght@300;400;600&display=swap">
<style>
  :root {
    --ink: #1e1e1e;
    --pink: #e0157f;
    --paper: #ffffff;
    --backdrop: #e9e9e9;
    --rule: #9a9a9a;
    --text: #2b2b2b;
  }
  * { margin: 0; padding: 0; box-sizing: border-box; }
  html, body { width: 1200px; height: 1200px; overflow: hidden; }
  body {
    background: var(--backdrop);
    font-family: "Montserrat", sans-serif;
    position: relative;
    color: var(--text);
  }
  .sheet, .card { position: absolute; box-shadow: 6px 8px 14px rgba(0,0,0,.35); }

  /* Letterhead */
  .letterhead {
    left: 268px; top: 170px; width: 667px; height: 863px;
    background: var(--paper);
  }
  .wordmark {
    font-family: "Montserrat", sans-serif;
    font-weight: 300;
    white-space: nowrap;
    letter-spacing: .5px;
  }
  .letterhead .wordmark {
    position: absolute; left: 0; right: 0; top: 248px;
    text-align: center; font-size: 31px; color: var(--ink);
  }
  .letterhead-footer {
    position: absolute; left: 0; right: 0; bottom: 0; height: 68px;
    background: var(--ink); color: #fff; text-align: center;
  }
  .footer-address {
    font-size: 12.5px; font-weight: 300; letter-spacing: 1px;
    padding-top: 14px;
  }
  .footer-rule {
    width: 515px; height: 1px; margin: 6px auto 0;
    background: #8a8a8a;
  }
  .footer-contacts {
    display: flex; justify-content: center; gap: 15px;
    margin-top: 6px; font-size: 12.5px; font-weight: 300; letter-spacing: .6px;
  }
  .contact-item { display: inline-flex; align-items: center; gap: 5px; white-space: nowrap; }
  .icon { width: 8px; height: 8px; fill: var(--pink); flex: none; }
  .footer-contacts .icon { width: 9px; height: 9px; }

  /* Business card front */
  .card { width: 351px; height: 200px; top: 358px; }
  .card-front { left: 92px; background: var(--paper); }
  .card-front .wordmark {
    position: absolute; right: 20px; top: 38px;
    font-size: 16.5px; color: var(--ink);
  }
  .holder-name {
    position: absolute; left: 20px; top: 109px;
    font-size: 14px; font-weight: 600; color: var(--pink); letter-spacing: .2px;
  }
  .holder-role {
    position: absolute; left: 20px; right: 20px; top: 125px;
    display: flex; align-items: center; gap: 4px;
    font-size: 8.2px; white-space: nowrap;
  }
  .holder-role::after {
    content: ""; flex: 1; height: 1px; background: var(--rule); margin-top: 5px;
  }
  .card-contacts {
    position: absolute; left: 20px; top: 146px;
    list-style: none; font-size: 8.2px; line-height: 12px;
  }
  .card-address {
    position: absolute; right: 20px; top: 158px;
    font-size: 8.2px; line-height: 12px; text-align: right;
  }
  .card-base {
    position: absolute; left: 0; right: 0; bottom: 0; height: 5px;
    background: var(--ink);
  }

  /* Business card back */
  .card-back { left: 781px; background: var(--ink); color: #fff; }
  .card-back .wordmark {
    position: absolute; left: 0; right: 0; top: 82px;
    text-align: center; font-size: 26px; color: #fff;
  }
  .card-url {
    position: absolute; left: 0; right: 0; top: 170px;
    text-align: center; font-size: 10px; letter-spacing: .6px;
  }
  .card-url .domain { color: var(--pink); font-weight: 600; }
</style>
</head>
<body>
<svg width="0" height="0" style="position:absolute" aria-hidden="true">
  <symbol id="i-phone" viewBox="0 0 16 16"><path d="M3.6 1.2l2.2 2.6c.4.5.3 1.1-.1 1.5L4.6 6.4c.9 2 2.6 3.7 4.9 4.9l1.1-1.1c.4-.4 1-.5 1.5-.1l2.6 2.2c.5.4.5 1.1.1 1.5l-1.3 1.3C10.4 16 .1 5.7 1 2.6L2.2 1.2c.4-.4 1-.4 1.4 0z"/></symbol>
  <symbol id="i-mail" viewBox="0 0 16 16"><path d="M1 3h14v1.2L8 8.6 1 4.2z"/><path d="M1 5.8l7 4.4 7-4.4V13H1z"/></symbol>
  <symbol id="i-globe" viewBox="0 0 16 16"><path d="M8 1a7 7 0 100 14A7 7 0 008 1zm5.4 6.2h-2.5a11 11 0 00-.9-4.3 5.6 5.6 0 013.4 4.3zM8 2.5c.7.9 1.3 2.6 1.4 4.7H6.6C6.7 5.1 7.3 3.4 8 2.5zM6 2.9a11 11 0 00-.9 4.3H2.6A5.6 5.6 0 016 2.9zM2.6 8.8h2.5c.1 1.6.4 3.1.9 4.3a5.6 5.6 0 01-3.4-4.3zM8 13.5c-.7-.9-1.3-2.6-1.4-4.7h2.8c-.1 2.1-.7 3.8-1.4 4.7zm2 -.4c.5-1.2.8-2.7.9-4.3h2.5A5.6 5.6 0 0110 13.1z"/></symbol>
</svg>

<section class="sheet letterhead" aria-label="Briefpapier">
  <div class="wordmark">Wiesentalblick</div>
  <footer class="letterhead-footer">
    <p class="footer-address">Talweg 14, 4418 Reigoldswil, Schweiz</p>
    <div class="footer-rule"></div>
    <div class="footer-contacts">
      <span class="contact-item"><svg class="icon"><use href="#i-phone"/></svg>+41 (0) 800 22 40 40</span>
      <span class="contact-item"><svg class="icon"><use href="#i-mail"/></svg>hallo@wiesentalblick.ch</span>
      <span class="contact-item"><svg class="icon"><use href="#i-globe"/></svg>www.wiesentalblick.ch</span>
    </div>
  </footer>
</section>

<section class="card card-front" aria-label="Visitenkarte Vorderseite">
  <div class="wordmark">Wiesentalblick</div>
  <h1 class="holder-name">DR. LENA ARNOLD</h1>
  <p class="holder-role">FÄ für Plastische Chirurgie</p>
  <ul class="card-contacts">
    <li class="contact-item"><svg class="icon"><use href="#i-phone"/></svg>061.555.2740</li><br>
    <li class="contact-item"><svg class="icon"><use href="#i-mail"/></svg>l.arnold@praxisarnold.ch</li><br>
    <li class="contact-item"><svg class="icon"><use href="#i-globe"/></svg>www.praxisarnold.ch</li>
  </ul>
  <p class="card-address">Talweg 14<br>4418 Reigoldswil, Schweiz</p>
  <div class="card-base"></div>
</section>

<section class="card card-back" aria-label="Visitenkarte Rückseite">
  <div class="wordmark">Wiesentalblick</div>
  <p class="card-url">www.<span class="domain">wiesentalblick</span>.ch</p>
</section>
</body>
</html>
```